Martial Arts & Fitness Center Website

We require a wordpress website for a martial arts and fitness company that is located in Stafford, Texas. The name of the facility is Copper Ridge Martial Arts. This company offers various fitness programs throughout the day, after school care with transportation included, and martial arts programs in the evening. Martial Arts programs in the evening is for beginners, intermediate and advanced students. We web design should be clean, crisp, vibrant, and modern. We also require in addition to the standard pages, at a minimum a contact us page, a registration page for various events at the school (lock-ins, parents night out, after school pickup, etc.) once registered we would like the site to have the option to pay for that service as well. We would like to have the ability to include a shopping cart so we can sell gear on the site.

Target Market(s)

Consumers with school age kids, martial artists, parents with kids in martial arts.

Industry/Entity Type

School

Requirements
Must have
• At least a registration page and contact us page. The ability to add more pages later.

School logo is currently being created and the colors is red, white and blue. Will upload logo as soon as it is received.

```html
<!DOCTYPE html>
<html lang="en">
<head>
<meta charset="utf-8">
<title>Copper Ridge Martial Arts</title>
<link href="https://fonts.googleapis.com/css2?family=PT+Sans:wght@400;700&family=PT+Sans+Narrow:wght@400;700&display=swap" rel="stylesheet">
<style>
:root{
  --navy:#132a7a;
  --navy-dark:#0d1f5c;
  --red:#c8141b;
  --red-dark:#a30d12;
  --text:#555;
  --text-dark:#333;
  --rule:#dcdcdc;
  --panel:#f6f6f6;
  --footer:#f1f1f1;
  --white:#fff;
}
*{box-sizing:border-box;margin:0;padding:0}
html,body{width:822px;height:1200px;overflow:hidden;background:var(--white)}
body{font-family:"PT Sans",Arial,sans-serif;color:var(--text);position:relative}
.abs{position:absolute}
.topline{left:0;top:0;width:822px;height:3px;background:#ddd}
.utility{right:34px;top:13px;display:flex;gap:14px;font-size:9.5px;color:#444}
.utility span{display:flex;align-items:center;gap:4px}
.brand{left:33px;top:33px;font-size:21px;color:var(--navy);letter-spacing:.2px}
.slogan{left:33px;top:59px;width:241px;text-align:right;font-size:10px;color:#333}
.search{left:604px;top:59px;width:186px;height:23px;border:1px solid #ccc;border-radius:2px;font-size:9px;font-style:italic;color:#888;padding:5px 10px}
.search svg{position:absolute;right:7px;top:5px}
.nav{left:26px;top:91px;width:770px;height:36px;background:linear-gradient(#e0252b,#b80f15);display:flex;border-radius:2px 2px 0 0}
.nav a{color:var(--white);text-decoration:none;font-size:12.5px;line-height:36px;text-align:center;border-right:1px solid #9e0d12;box-shadow:1px 0 0 #e9494e}
.nav a:last-child{border:none;box-shadow:none}
.hero{left:27px;top:128px;width:769px;height:309px;border:1px solid #ddd;background:#f7f7f8}
.hero-photo{position:absolute;left:0;top:0;width:538px;height:307px;background:linear-gradient(120deg,#e9eaec 0%,#d2d4d8 45%,#b9bcc4 70%,#e2e3e6 100%)}
.hero-copy{position:absolute;left:561px;top:28px;width:175px;color:var(--navy)}
.hero-copy h1{font-family:"PT Sans Narrow",sans-serif;font-weight:700;font-size:20px;line-height:23px}
.hero-copy h2{font-family:"PT Sans Narrow",sans-serif;font-weight:400;font-size:19px;line-height:22px;margin-bottom:8px}
.hero-copy p{font-size:9.2px;line-height:15px;margin-bottom:6px}
.btn-navy{display:inline-block;background:var(--navy);color:var(--white);font-size:10px;padding:5px 14px;margin-top:6px;border-radius:2px}
.dots{position:absolute;right:14px;bottom:15px;display:flex;gap:3px}
.dots span{width:15px;height:15px;border-radius:50%;background:#d9deef;color:var(--navy);font-size:8px;text-align:center;line-height:15px}
.dots span.on{background:var(--navy);color:var(--white)}
.h-navy{font-family:"PT Sans Narrow",sans-serif;font-weight:700;color:var(--navy-dark);font-size:16.5px}
.h-red{font-family:"PT Sans Narrow",sans-serif;font-weight:700;color:var(--red);font-size:15px}
.welcome{left:27px;top:457px;width:530px}
.welcome p{font-size:8.8px;line-height:15px;margin-top:4px;color:#5a5a5a}
.welcome p+p{margin-top:6px}
.vrule{left:579px;top:465px;width:1px;height:482px;background:var(--rule)}
.hrule{top:595px;height:1px;background:var(--rule)}
.train{left:598px;top:455px}
.train-photo{left:595px;top:479px;width:63px;height:78px;background:linear-gradient(#e5ddd5,#c9b9ab)}
.train-text{left:688px;top:479px;width:97px;font-size:8.8px;line-height:15px;text-align:justify;color:#666}
.btn-light{left:689px;top:545px;width:65px;height:21px;background:#eee;border:1px solid #e0e0e0;font-family:"PT Sans Narrow",sans-serif;font-weight:700;font-size:9.5px;color:var(--red);text-align:center;line-height:19px}
.classes-title{left:23px;top:607px}
.classes{left:22px;top:638px;width:550px;display:grid;grid-template-columns:repeat(3,173px);column-gap:15px;row-gap:11px}
.class-photo{width:173px;height:89px;border:1px solid #e4e4e4}
.class h3{font-family:"PT Sans Narrow",sans-serif;font-weight:700;font-size:10px;color:#333;margin-top:7px}
.class p{font-size:8px;line-height:15px;color:#666}
.shop{left:589px;top:602px;width:199px;height:380px;background:#fbfbfb;border:1px solid #eee;box-shadow:0 0 4px rgba(0,0,0,.06)}
.shop h2{position:absolute;left:22px;top:12px}
.product{position:absolute;left:22px;width:170px;height:64px}
.product-photo{position:absolute;left:0;top:0;width:84px;height:64px;background:var(--white);border:1px solid #e3e3e3;box-shadow:0 1px 2px rgba(0,0,0,.08)}
.product-photo i{position:absolute;left:14px;top:10px;width:56px;height:44px;border-radius:10px;background:linear-gradient(135deg,#3b5fd6,#0f2a8a)}
.product-photo i.dark{background:linear-gradient(135deg,#555,#111);height:24px;top:20px;border-radius:12px}
.product .name{position:absolute;left:97px;top:0;font-size:10.5px;color:#444}
.product .price{position:absolute;left:97px;top:16px;font-size:13px;color:#333}
.product .add{position:absolute;left:97px;top:38px;width:54px;height:18px;background:var(--red);color:var(--white);font-size:7.5px;text-align:center;line-height:18px;border-radius:1px}
.view-more{position:absolute;left:131px;top:352px;width:57px;height:17px;background:#eee;font-family:"PT Sans Narrow",sans-serif;font-weight:700;font-size:8.5px;color:var(--red);text-align:center;line-height:17px}
.footer{left:0;top:990px;width:822px;height:173px;background:linear-gradient(#ececec,#f7f7f7 30%,#f7f7f7)}
.fcol{position:absolute;top:24px}
.fcol h4{font-weight:400;font-size:11.5px;color:#333;margin-bottom:8px}
.fcol a{display:block;font-size:9px;line-height:17.3px;color:#555;text-decoration:none}
.fdiv{position:absolute;top:30px;width:1px;height:98px;background:#ddd}
.social{display:flex;gap:5px;margin-top:2px}
.social span{width:18px;height:18px;border-radius:2px}
.bottom{left:0;top:1163px;width:822px;height:37px;background:#f3f3f3;border-top:1px solid #e2e2e2;font-size:8px;color:#555}
.bottom .copy{position:absolute;left:35px;top:13px}
.bottom .legal{position:absolute;right:25px;top:13px}
</style>
</head>
<body>
<div class="abs topline"></div>

<header>
  <div class="abs utility">
    <span><svg width="13" height="11" viewBox="0 0 13 11"><path d="M0 1h2l2 6h7l1.5-4.5H3" fill="none" stroke="#777" stroke-width="1.4"/><circle cx="5" cy="9.5" r="1.2" fill="#777"/><circle cx="10" cy="9.5" r="1.2" fill="#777"/></svg>Shopping Cart</span>
    <span><svg width="12" height="12" viewBox="0 0 12 12"><circle cx="6" cy="3.5" r="3" fill="#777"/><path d="M0 12c0-4 2.5-5.5 6-5.5s6 1.5 6 5.5z" fill="#777"/></svg>Register Now</span>
    <span><svg width="13" height="12" viewBox="0 0 13 12"><rect x="0" y="5" width="3" height="7" fill="#777"/><path d="M4 5l3-5c1.5 0 1.5 1.5 1 4h4v3l-2 5H4z" fill="#777"/></svg>Sign Up</span>
  </div>
  <div class="abs brand">Copper Ridge Martial Arts</div>
  <div class="abs slogan">your slogan goes here</div>
  <div class="abs search">Search here..
    <svg width="12" height="12" viewBox="0 0 12 12"><circle cx="5" cy="5" r="3.8" fill="none" stroke="#555" stroke-width="1.6"/><path d="M8 8l3.3 3.3" stroke="#555" stroke-width="1.8"/></svg>
  </div>
  <nav class="abs nav">
    <a style="width:82px">Home</a>
    <a style="width:85px">Courses</a>
    <a style="width:89px">Lock-ins</a>
    <a style="width:134px">Parents Nightout</a>
    <a style="width:116px">School Pickup</a>
    <a style="width:90px">Register</a>
    <a style="width:174px;text-align:left;padding-left:24px">Contact us</a>
  </nav>
</header>

<section class="abs hero">
  <div class="hero-photo" role="img" aria-label="Students in white uniforms with blue belts practising stances in a training hall"></div>
  <div class="hero-copy">
    <h1>Martial Arts Training</h1>
    <h2>Join Us Now</h2>
    <p>Pellentesque habitant morbi tristique senectus et netus et malesuada.</p>
    <p>Fames ac turpis egestas. In posuere felis nec tortor. Pellentesque faucibus. Ut accumsan ultricies elit. Maecenas at justo id velit placerat molestie. Donec dictum lectus non odio.Donec convallis pede venenatis nibh. Duis quam. Nam eget lacus. Aliquam erat volutpat. Quisque dignissim congue leo.</p>
    <span class="btn-navy">Register Now</span>
  </div>
  <div class="dots"><span class="on">1</span><span>2</span><span>3</span><span>4</span></div>
</section>

<section class="abs welcome">
  <h2 class="h-navy">Welcome to Copper Ridge Martial Arts</h2>
  <p>Lorem ipsum dolor sit amet, consectetuer adipiscing elit. Nam cursus. Morbi ut mi. Nullam enim leo, egestas id, condimentum at, laoreet mattis, massa. Sed eleifend nonummy diam.</p>
  <p>Praesent mauris ante, elementum et, bibendum at, posuere sit amet, nibh. Duis tincidunt lectus quis dui viverra vestibulum. Suspendisse vulputate aliquam dui. Nulla elementum dui ut augue. Aliquam vehicula mi at mauris. Maecenas placerat, nisl at consequat rhoncus, sem nunc gravida justo, quis eleifend arcu velit quis lacus. Morbi magna magna, tincidunt a, mattis non, imperdiet vitae, tellus. Sed odio est, auctor ac, sollicitudin in, consequat vitae, orci. Fusce id felis. Vivamus sollicitudin metus eget eros.</p>
</section>

<div class="abs vrule"></div>
<div class="abs hrule" style="left:30px;width:548px"></div>
<div class="abs hrule" style="left:583px;width:211px"></div>

<h2 class="abs h-red train">How We Train Students</h2>
<div class="abs train-photo" role="img" aria-label="Group of smiling young students in uniforms"></div>
<p class="abs train-text">Cum sociis natoque penatibus et magnis dis parturient montes, nascetur ridiculus</p>
<div class="abs btn-light">Learn More</div>

<h2 class="abs h-navy classes-title">Our Classes &amp; Training</h2>
<section class="abs classes">
  <article class="class"><div class="class-photo" role="img" aria-label="Instructor guiding a young child outdoors" style="background:linear-gradient(#d9dfd0,#a9bf86)"></div><h3>Duis non nunc. Nulla rhoncus</h3><p>Ut velit enim, vestibulum non, fermentum nec, hendrerit quis, leo. Pellentesque</p></article>
  <article class="class"><div class="class-photo" role="img" aria-label="Close view of a belt being tied on a white uniform" style="background:linear-gradient(110deg,#ece9e6,#b6a79a 60%,#e5e1dd)"></div><h3>Duis non nunc. Nulla rhoncus</h3><p>Ut velit enim, vestibulum non, fermentum nec, hendrerit quis, leo. Pellentesque</p></article>
  <article class="class"><div class="class-photo" role="img" aria-label="Two students practising a kata against a bright sky" style="background:linear-gradient(#dfe8f0,#f4f6f8)"></div><h3>Duis non nunc. Nulla rhoncus</h3><p>Ut velit enim, vestibulum non, fermentum nec, hendrerit quis, leo. Pellentesque</p></article>
  <article class="class"><div class="class-photo" role="img" aria-label="Student kicking a pad held by a partner" style="background:linear-gradient(110deg,#d8c9b3,#efe6d8 60%,#c9b79d)"></div><h3>Duis non nunc. Nulla rhoncus</h3><p>Ut velit enim, vestibulum non, fermentum nec, hendrerit quis, leo. Pellentesque</p></article>
  <article class="class"><div class="class-photo" role="img" aria-label="Row of children in uniforms with coloured belts" style="background:linear-gradient(#b8824f,#d9c3a6 55%,#3a55b8)"></div><h3>Duis non nunc. Nulla rhoncus</h3><p>Ut velit enim, vestibulum non, fermentum nec, hendrerit quis, leo. Pellentesque</p></article>
  <article class="class"><div class="class-photo" role="img" aria-label="Class of students performing kicks in a bright studio" style="background:linear-gradient(#eef0f2,#cfd2d6)"></div><h3>Duis non nunc. Nulla rhoncus</h3><p>Ut velit enim, vestibulum non, fermentum nec, hendrerit quis, leo. Pellentesque</p></article>
</section>

<aside class="abs shop">
  <h2 class="h-red">Buy Our Products</h2>
  <div class="product" style="top:44px"><div class="product-photo" role="img" aria-label="Blue sparring gloves"><i></i></div><span class="name">Product Name</span><span class="price">$24.99</span><span class="add">Add to Cart</span></div>
  <div class="product" style="top:123px"><div class="product-photo" role="img" aria-label="Blue sparring foot guards"><i></i></div><span class="name">Product Name</span><span class="price">$24.99</span><span class="add">Add to Cart</span></div>
  <div class="product" style="top:197px"><div class="product-photo" role="img" aria-label="Blue sparring headgear"><i></i></div><span class="name">Product Name</span><span class="price">$24.99</span><span class="add">Add to Cart</span></div>
  <div class="product" style="top:273px"><div class="product-photo" role="img" aria-label="Black kicking paddle"><i class="dark"></i></div><span class="name">Product Name</span><span class="price">$24.99</span><span class="add">Add to Cart</span></div>
  <div class="view-more">VIEW MORE</div>
</aside>

<footer class="abs footer">
  <div class="fcol" style="left:48px"><h4>Quick Links</h4><a>Home</a><a>About Us</a><a>How We Train</a><a>Register Now</a></div>
  <div class="fdiv" style="left:139px"></div>
  <div class="fcol" style="left:170px"><h4>Courses</h4><a>Praesent vitae</a><a>Ut velit enim</a><a>Vestibulum non</a><a>Fermentum nec</a></div>
  <div class="fdiv" style="left:263px"></div>
  <div class="fcol" style="left:287px"><h4>Courses</h4><a>Praesent vitae</a><a>Ut velit enim</a><a>Vestibulum non</a><a>Fermentum nec</a></div>
  <div class="fdiv" style="left:379px"></div>
  <div class="fcol" style="left:409px"><h4>Support</h4><a>Testimonials</a><a>Blog</a><a>Why We Are</a><a>Our Trainers</a></div>
  <div class="fdiv" style="left:498px"></div>
  <div class="fcol" style="left:533px"><h4>Contact</h4><a>Sitemap</a><a>Shopping Cart</a><a>Location</a><a>Contact Info</a></div>
  <div class="fdiv" style="left:624px"></div>
  <div class="fcol" style="left:646px"><h4>Get In Touch</h4>
    <div class="social"><span style="background:#2f5aa8"></span><span style="background:#2a7fb8"></span><span style="background:#e8762b"></span><span style="background:#c9302c"></span></div>
  </div>
</footer>

<div class="abs bottom">
  <span class="copy">Copyright © 1997-2012 Ridgeline Web Studio All Rights Reserved.</span>
  <span class="legal">Privacy Policy &nbsp;|&nbsp; Terms of Services</span>
</div>
</body>
</html>
```